PLUX Safety Poster

We need a safety poster designed that we can provide to our members to put up on the wall of their factories. It needs to be clear and concise and simple but also that they are aware it is provided by us. We would like the poster to be in line with our branding companies, you can view these on our website www.brightvellum.com A3 size please

All files are here https://www.filequay.com/sh/wq7tn2bz5mc8xpe/QRfTzk-LmPaVuWx84Hc3Jb6s?n=47719305

```html
<!DOCTYPE html>
<html lang="en">
<head>
<meta charset="utf-8">
<title>PLUX Safety Poster – Heat Stress</title>
<link href="https://fonts.googleapis.com/css2?family=Montserrat:wght@800;900&family=Open+Sans:ital,wght@0,400;0,600;0,700;1,400&display=swap" rel="stylesheet">
<style>
  :root{
    --purple-deep:#3c0f4f;
    --purple:#5e1a72;
    --magenta:#b3125f;
    --red:#d81f2c;
    --red-dark:#9e0d2a;
    --orange:#f47a1f;
    --yellow:#fbc531;
    --white:#ffffff;
    --pink-light:#ffe3ea;
  }
  *{box-sizing:border-box;margin:0;padding:0}
  html,body{width:874px;height:1200px;overflow:hidden;background:var(--purple-deep)}
  .poster{position:relative;width:874px;height:1200px;overflow:hidden;font-family:"Open Sans",Arial,sans-serif;color:var(--white)}
  .poster-art{position:absolute;inset:0}
  .warning-icon{position:absolute;left:357px;top:60px;width:160px;height:140px}
  .headline{position:absolute;left:0;right:0;top:218px;text-align:center;font-family:"Montserrat",Arial,sans-serif;font-weight:900;font-size:104px;line-height:.98;letter-spacing:1px;text-transform:uppercase;text-shadow:0 4px 10px rgba(60,0,30,.45)}
  .thermometer{position:absolute;left:46px;top:452px;width:270px;height:330px;border-radius:12px;background:radial-gradient(ellipse at 40% 55%,#ffd34d 0%,#f47a1f 40%,rgba(216,31,44,.6) 70%,rgba(216,31,44,0) 100%)}
  .tips{position:absolute;left:318px;top:452px;list-style:none}
  .tip{display:flex;align-items:center;gap:14px;height:58px;font-size:21px;font-weight:600}
  .tip svg{width:40px;height:40px;flex:none}
  .signs{position:absolute;left:64px;right:64px;top:842px}
  .signs-title{font-family:"Montserrat",Arial,sans-serif;font-weight:800;font-size:33px;color:var(--yellow);margin-bottom:18px}
  .signs-list{list-style:none;font-size:21px;line-height:1.85;color:var(--pink-light)}
  .signs-note{margin-top:18px;font-size:16px;font-style:italic;line-height:1.45;color:var(--pink-light)}
  .footer{position:absolute;left:0;right:0;bottom:0;height:68px;background:var(--purple-deep);display:flex;align-items:center;justify-content:space-between;padding:0 48px;font-size:15px}
  .brand{display:flex;align-items:center;gap:10px;font-weight:700;font-size:22px;letter-spacing:2px}
  .brand-dot{width:22px;height:22px;border-radius:50%;background:var(--white)}
</style>
</head>
<body>
<main class="poster">
  <svg class="poster-art" viewBox="0 0 874 1200" aria-hidden="true">
    <defs>
      <linearGradient id="bg" x1="0" y1="0" x2="0" y2="1">
        <stop offset="0" stop-color="#5e1a72"/>
        <stop offset=".55" stop-color="#b3125f"/>
        <stop offset="1" stop-color="#7a0f4a"/>
      </linearGradient>
      <linearGradient id="flare" x1="0" y1="0" x2="1" y2="0">
        <stop offset="0" stop-color="#fbc531"/>
        <stop offset=".5" stop-color="#f47a1f"/>
        <stop offset="1" stop-color="#d81f2c"/>
      </linearGradient>
      <linearGradient id="lower" x1="0" y1="0" x2="0" y2="1">
        <stop offset="0" stop-color="#d81f2c"/>
        <stop offset="1" stop-color="#8a0d3f"/>
      </linearGradient>
    </defs>
    <rect width="874" height="1200" fill="url(#bg)"/>
    <path d="M0 300 C220 170 560 120 874 170 L874 250 C600 200 300 250 0 390 Z" fill="url(#flare)" opacity=".9"/>
    <path d="M0 250 C250 130 600 90 874 120 L874 150 C600 120 260 170 0 290 Z" fill="#fbc531" opacity=".55"/>
    <path d="M0 840 C260 770 600 760 874 700 L874 1200 L0 1200 Z" fill="url(#flare)"/>
    <path d="M0 870 C280 800 620 790 874 735 L874 1200 L0 1200 Z" fill="url(#lower)"/>
  </svg>

  <svg class="warning-icon" viewBox="0 0 160 140" role="img" aria-label="Warning sign">
    <path d="M80 8 L152 132 L8 132 Z" fill="#d81f2c" stroke="#ffffff" stroke-width="9" stroke-linejoin="round"/>
    <rect x="73" y="46" width="14" height="50" rx="6" fill="#ffffff"/>
    <circle cx="80" cy="112" r="8" fill="#ffffff"/>
  </svg>

  <h1 class="headline">Heat Stress<br>Isn’t Cool</h1>

  <div class="thermometer" role="img" aria-label="Thermometer showing high temperature against a hot sun"></div>

  <ul class="tips">
    <li class="tip">
      <svg viewBox="0 0 40 40"><circle cx="20" cy="20" r="18" fill="none" stroke="#fff" stroke-width="2.5"/><path d="M20 9 C14 18 13 21 13 24 a7 7 0 0 0 14 0 c0-3-1-6-7-15z" fill="#fff"/></svg>
      Drink Plenty Of Water
    </li>
    <li class="tip">
      <svg viewBox="0 0 40 40"><circle cx="20" cy="20" r="18" fill="none" stroke="#fff" stroke-width="2.5"/><circle cx="20" cy="20" r="10" fill="none" stroke="#fff" stroke-width="2.5"/><path d="M20 14 V20 H25" stroke="#fff" stroke-width="2.5" fill="none"/></svg>
      Take Breaks
    </li>
    <li class="tip">
      <svg viewBox="0 0 40 40"><circle cx="20" cy="20" r="18" fill="none" stroke="#fff" stroke-width="2.5"/><path d="M14 11 L10 16 L13 19 L14 17 V29 H26 V17 L27 19 L30 16 L26 11 H23 a3 3 0 0 1 -6 0 Z" fill="#fff"/></svg>
      Wear Light Clothing Where Appropriate
    </li>
    <li class="tip">
      <svg viewBox="0 0 40 40"><circle cx="20" cy="20" r="18" fill="none" stroke="#fff" stroke-width="2.5"/><path d="M8 20 C13 12 27 12 32 20 C27 28 13 28 8 20 Z" fill="none" stroke="#fff" stroke-width="2.5"/><circle cx="20" cy="20" r="4" fill="#fff"/></svg>
      Monitor Workmates For Signs Of Heat Stress
    </li>
  </ul>

  <section class="signs">
    <h2 class="signs-title">Signs Of Heat Stress Or Heat Exhaustion</h2>
    <ul class="signs-list">
      <li>Feeling Sick, Weak Or Clumsy / Dizzy</li>
      <li>Cramps Can Also Be Caused By Heat</li>
      <li>Discomfort From Heat Rash</li>
    </ul>
    <p class="signs-note">**If you have profuse sweating, weakness, nausea or vomiting, headaches and muscle spasms then stop work immediately and seek help</p>
  </section>

  <footer class="footer">
    <span>This is an PLUX Safety Poster</span>
    <span class="brand"><span class="brand-dot"></span>PLUX</span>
  </footer>
</main>
</body>
</html>
```